Window cleaning company in need of leaflet design

Family run business requires leaflet design.
Our company uses water fed pole with pure water which is what the leaflet needs to emphasise on (include a background picture of a water fed pole cleaning a window.)

other services we offer which i would like to include are:
• facia/soffit cleaning.
• Conservatory cleans.
• Gutter clearing which is performed by a gutter vacuum pictures of gutters before and after clean are provided to every customer if they require.
• pressure washing

uploaded company logo to be included on leaflet.
number to include is 07715264389
email address is Rtglasscare@mailbay.test
would also like a facebook symbol included to show we are on social media.
Thank you

Font styles to use
Serif
Sans Serif

Colors
00a990
33a6d7
3276b5
3277b5
34a7d8
87cfc6
33b8a4
cfdfed
85acd3

Requirements
Must have
• We use traditional and water fed pole methods of cleaning. So those hard to reach or awkward to clean windows are not a problem. No need for ladders.

Our water fed pole system uses 100% pure water. This is water that has been de-ironised and de-mineralised to ensue it’s perfectly pure for a spot free finish.

• fully insured

• regular and reliable service
• one off cleans available

Call dean on 07715264389 for a free quote

```html
<!DOCTYPE html>
<html lang="en">
<head>
<meta charset="utf-8">
<title>R.T Window Care – Leaflet</title>
<link href="https://fonts.googleapis.com/css2?family=Poppins:wght@300;400;500;600;700;800&display=swap" rel="stylesheet">
<style>
  :root {
    --page-bg: #dcdcdc;
    --navy: #1c2a6b;
    --royal: #1d33ea;
    --royal-deep: #1a2bd6;
    --royal-light: #2a4cf5;
    --silver: #c9ccd3;
    --sky-top: #3d7fd9;
    --sky-mid: #8ab8ea;
    --sky-light: #d7e8f8;
    --white: #ffffff;
    --ink-soft: #2b3a6e;
    --tick: #3b64e0;
    --yellow: #f5ef1a;
  }
  * { box-sizing: border-box; margin: 0; padding: 0; }
  html, body { width: 1200px; height: 2400px; overflow: hidden; }
  body { background: var(--page-bg); font-family: "Poppins", sans-serif; position: relative; }

  .leaflet {
    position: absolute; left: 60px; top: 436px;
    width: 1080px; height: 1528px;
    background: var(--white);
    box-shadow: 0 6px 18px rgba(0,0,0,.25);
    overflow: hidden;
  }

  /* Hero */
  .hero { position: absolute; left: 0; top: 0; width: 1080px; height: 746px; }
  .hero-photo {
    position: absolute; left: 0; top: 0; width: 1080px; height: 600px;
    background: radial-gradient(ellipse at 70% 30%, var(--sky-light) 0%, transparent 45%),
                radial-gradient(ellipse at 20% 70%, #e6f0fb 0%, transparent 40%),
                linear-gradient(160deg, var(--sky-top) 0%, var(--sky-mid) 55%, var(--sky-light) 100%);
  }
  .hero-waves { position: absolute; left: 0; top: 0; width: 1080px; height: 746px; }
  .headline {
    position: absolute; left: 54px; top: 58px;
    color: var(--white); font-weight: 700; font-size: 104px; line-height: .92;
    letter-spacing: 1px; text-transform: uppercase;
  }
  .brand {
    position: absolute; left: 62px; top: 662px;
    color: var(--navy); font-weight: 600; font-size: 36px; letter-spacing: -.3px;
  }
  .hero-services {
    position: absolute; left: 478px; top: 650px;
    display: grid; grid-template-columns: auto auto; column-gap: 16px; row-gap: 8px;
    list-style: none; color: var(--ink-soft); font-weight: 500; font-size: 21px;
    text-transform: uppercase;
  }
  .hero-services li { display: flex; align-items: center; gap: 6px; white-space: nowrap; }
  .hero-services svg { width: 16px; height: 16px; }

  .divider { position: absolute; left: 0; top: 746px; width: 1080px; height: 12px;
    background: linear-gradient(180deg, #eef0f3, var(--silver)); }

  /* Blue panel */
  .info {
    position: absolute; left: 0; top: 758px; width: 1080px; height: 673px;
    background: linear-gradient(120deg, var(--royal-deep) 0%, var(--royal) 55%, var(--royal-light) 100%);
    color: var(--white);
  }
  .info-title { position: absolute; left: 69px; top: 56px; font-size: 50px; font-weight: 500; }
  .services-heading { position: absolute; left: 69px; top: 140px; font-size: 30px; font-weight: 500; }
  .service-list {
    position: absolute; left: 63px; top: 200px; width: 560px;
    display: grid; grid-template-columns: 282px auto; row-gap: 16px;
    list-style: none; font-size: 18px; font-weight: 500; text-transform: uppercase;
  }
  .service-list li { display: flex; align-items: center; gap: 9px; white-space: nowrap; }
  .service-list svg { width: 22px; height: 22px; }
  .about {
    position: absolute; left: 69px; top: 318px; width: 533px;
    font-size: 16.5px; font-weight: 300; line-height: 23px; text-align: justify;
    color: #dfe6ff;
  }
  .gallery { position: absolute; left: 623px; top: 152px; width: 400px; height: 268px; }
  .gallery .shot {
    position: absolute; width: 184px; height: 122px; border-radius: 9px;
    border: 2px solid rgba(255,255,255,.85);
  }
  .shot-house { left: 0; top: 0; background: linear-gradient(160deg, #c9d3dc, #8a6a5a 60%, #6f7e5a); }
  .shot-pole { left: 214px; top: 0; background: linear-gradient(180deg, #8fb3e0, #2a3340 55%, #d5dbe0); }
  .shot-vacuum { left: 0; top: 146px; background: linear-gradient(150deg, #57606a, #9a8d3c 55%, #3c4248); }
  .shot-lift { left: 214px; top: 146px; background: linear-gradient(160deg, #a9c4e8 0%, #d9262b 40%, #c21d22 100%); }

  .quote-title { position: absolute; left: 60px; top: 508px; font-size: 30px; font-weight: 500; }
  .quote-line { position: absolute; left: 61px; top: 546px; font-size: 26px; font-weight: 500; }
  .quote-line .phone { color: var(--yellow); font-size: 40px; font-weight: 500; vertical-align: -2px; }
  .social { position: absolute; left: 60px; top: 598px; font-size: 26px; font-weight: 500;
    display: flex; align-items: center; gap: 18px; }
  .social .dot { width: 24px; height: 24px; border-radius: 50%; background: var(--white); }

  /* Footer */
  .contact-bar {
    position: absolute; left: 0; top: 1431px; width: 1080px; height: 97px;
    border-top: 6px solid var(--silver);
    display: flex; align-items: center; justify-content: center; gap: 14px;
    color: var(--navy); font-size: 28px; font-weight: 600; white-space: nowrap;
  }
  .contact-bar .sep { width: 2px; height: 34px; background: var(--navy); }
</style>
</head>
<body>
<main class="leaflet">
  <section class="hero">
    <div class="hero-photo" role="img" aria-label="Photo of a water fed pole squeegee held by a hand, cleaning a wet window against a blue cloudy sky"></div>
    <svg class="hero-waves" viewBox="0 0 1080 746" aria-hidden="true">
      <path d="M0,408 C180,378 340,398 470,468 C600,538 820,556 1080,388 L1080,746 L0,746 Z" fill="#c9ccd3"/>
      <path d="M0,424 C180,396 340,416 470,486 C600,556 820,574 1080,404 L1080,746 L0,746 Z" fill="#1d33ea"/>
      <path d="M0,448 C200,428 360,468 480,520 C620,580 840,586 1080,438 L1080,746 L0,746 Z" fill="#ffffff"/>
      <path d="M600,556 C760,596 920,574 1080,470" fill="none" stroke="#1d33ea" stroke-width="8"/>
    </svg>
    <h1 class="headline">Windows<br>Dirty?</h1>
    <div class="brand">R.T Window Care</div>
    <ul class="hero-services">
      <li><svg viewBox="0 0 16 16"><circle cx="8" cy="8" r="6.5" fill="none" stroke="var(--tick)" stroke-width="1.5"/><path d="M4.8 8.2l2.2 2.2 4.2-4.4" fill="none" stroke="var(--tick)" stroke-width="1.6"/></svg>Facia/Soffit Cleaning.</li>
      <li><svg viewBox="0 0 16 16"><circle cx="8" cy="8" r="6.5" fill="none" stroke="var(--tick)" stroke-width="1.5"/><path d="M4.8 8.2l2.2 2.2 4.2-4.4" fill="none" stroke="var(--tick)" stroke-width="1.6"/></svg>Gutter Clearing</li>
      <li><svg viewBox="0 0 16 16"><circle cx="8" cy="8" r="6.5" fill="none" stroke="var(--tick)" stroke-width="1.5"/><path d="M4.8 8.2l2.2 2.2 4.2-4.4" fill="none" stroke="var(--tick)" stroke-width="1.6"/></svg>Conservatory Cleans.</li>
      <li><svg viewBox="0 0 16 16"><circle cx="8" cy="8" r="6.5" fill="none" stroke="var(--tick)" stroke-width="1.5"/><path d="M4.8 8.2l2.2 2.2 4.2-4.4" fill="none" stroke="var(--tick)" stroke-width="1.6"/></svg>Pressure Washing</li>
    </ul>
  </section>

  <div class="divider"></div>

  <section class="info">
    <h2 class="info-title">R.T Window Care</h2>
    <h3 class="services-heading">Our Services Include:</h3>
    <ul class="service-list">
      <li><svg viewBox="0 0 22 22"><circle cx="11" cy="11" r="11" fill="#fff"/><path d="M9 6.5l4.5 4.5L9 15.5" fill="none" stroke="var(--royal)" stroke-width="2.6"/></svg>Facia/Soffit Cleaning</li>
      <li><svg viewBox="0 0 22 22"><circle cx="11" cy="11" r="11" fill="#fff"/><path d="M9 6.5l4.5 4.5L9 15.5" fill="none" stroke="var(--royal)" stroke-width="2.6"/></svg>Conservatory Cleans</li>
      <li><svg viewBox="0 0 22 22"><circle cx="11" cy="11" r="11" fill="#fff"/><path d="M9 6.5l4.5 4.5L9 15.5" fill="none" stroke="var(--royal)" stroke-width="2.6"/></svg>Gutter Clearing</li>
      <li><svg viewBox="0 0 22 22"><circle cx="11" cy="11" r="11" fill="#fff"/><path d="M9 6.5l4.5 4.5L9 15.5" fill="none" stroke="var(--royal)" stroke-width="2.6"/></svg>Pressure Washing</li>
    </ul>
    <p class="about">We use traditional and water fed pole methods of cleaning. So those hard to reach or awkward to clean windows are not a problem. No need for ladders.Our water fed pole system uses 100% pure water. This is water that has been de-ironised and de-mineralised to ensue it’s perfectly pure for a spot free finish. fully insured. Regular and reliable service.One off cleans available.</p>

    <div class="gallery">
      <div class="shot shot-house" role="img" aria-label="Photo of a house front being window cleaned with a water fed pole"></div>
      <div class="shot shot-pole" role="img" aria-label="Photo of a cleaner washing a conservatory roof"></div>
      <div class="shot shot-vacuum" role="img" aria-label="Photo of a gutter vacuum machine with hoses on a driveway"></div>
      <div class="shot shot-lift" role="img" aria-label="Photo of a worker on a lift pressure washing a red building facade"></div>
    </div>

    <div class="quote-title">Instant Quote</div>
    <div class="quote-line">Call Dean on <span class="phone">07715264389</span> for a free quote</div>
    <div class="social">Find Us On <span class="dot"></span></div>
  </section>

  <footer class="contact-bar">
    <span>R.T Window Care</span><span class="sep"></span>
    <span>Rtglasscare@mailbay.test</span><span class="sep"></span>
    <span>07715264389</span>
  </footer>
</main>
</body>
</html>
```